Kestrel Works Wall Art Design

Our local government has developed a department called the "Kestrel Works" which has been running for a few years. Our purpose is to encourage staff to think Under the Willow and engage their problems in new ways. We offer tools and services which enable collaboration between people and other departments, one such tool is our new meeting room. We've designed this space with the intention of encouraging creativity and allowing staff members to break away from the ordinary working environment. Attached are photos of the room.
The room is called "Under the Willow". In one photo you will see our Under the Willow sign filling the space where'd we'd like to have the design on, however we would like to stay away from naming labels in our design to convey to staff that this is their space as well, rather than the Kestrel Works' special little room. We would like a design that embodies the spirit of our department. We've talked about what that means to us and we've stepped it out as;
Investigate
Collaborate
Innovate
Create
Celebrate
We had ideas of having a funky word jumble design or something creative to use these words, but we'd love to see anything else that conveys a feeling of creativity.
The size of the art is limited to 1400mm x 2800mm

```html
<!DOCTYPE html>
<html lang="en">
<head>
<meta charset="utf-8">
<title>Kestrel Works – Under the Willow Wall Art</title>
<link rel="stylesheet" href="https://fonts.googleapis.com/css2?family=Playfair+Display:wght@900&family=Great+Vibes&family=Baloo+2:wght@800&family=Abril+Fatface&family=Limelight&display=swap">
<style>
  :root {
    --scene-top: #d3ebf4;
    --scene-mid: #9fd0df;
    --scene-bottom: #3f8c9c;
    --brick: #c2452d;
    --pillar: #7d7f83;
    --pillar-dark: #4d4f53;
    --label-shadow: #2b2b2b;
    --cream: #fdf8d8;
    --white: #ffffff;
    --silver: #e4e4e6;
    --lavender: #c9c5e2;
    --red: #e3343a;
    --red-dark: #8f2c1b;
    --blue: #1590d8;
    --navy: #2e3a8c;
    --ink: #1c1c1c;
  }
  html, body {
    margin: 0;
    padding: 0;
    overflow: hidden;
    background: #ffffff;
  }
  .wall-art {
    display: block;
    width: 1200px;
    height: 609px;
  }
  .word { dominant-baseline: middle; text-anchor: middle; }
  .word--celebrate { font-family: "Playfair Display", serif; font-weight: 900; font-size: 96px; fill: var(--red); }
  .word--create { font-family: "Great Vibes", cursive; font-size: 112px; fill: var(--red); stroke: var(--red-dark); stroke-width: 1.2; }
  .word--collaborate { font-family: "Baloo 2", sans-serif; font-weight: 800; font-size: 84px; fill: var(--blue); }
  .word--collaborate-shadow { font-family: "Baloo 2", sans-serif; font-weight: 800; font-size: 84px; fill: var(--label-shadow); }
  .word--innovate { font-family: "Abril Fatface", serif; font-size: 92px; fill: var(--navy); }
  .word--investigate { font-family: "Limelight", sans-serif; font-size: 56px; fill: var(--white); stroke: var(--ink); stroke-width: 2.4; paint-order: stroke; }
  .label-shadow { fill: var(--label-shadow); }
</style>
</head>
<body>
<svg class="wall-art" viewBox="0 0 1200 609" xmlns="http://www.w3.org/2000/svg" aria-labelledby="art-title">
  <title id="art-title">Celebrate, Create, Collaborate, Innovate, Investigate</title>
  <defs>
    <linearGradient id="scene-fill" x1="0" y1="0" x2="0" y2="1">
      <stop offset="0" stop-color="var(--scene-top)"/>
      <stop offset="0.45" stop-color="var(--scene-mid)"/>
      <stop offset="1" stop-color="var(--scene-bottom)"/>
    </linearGradient>
  </defs>

  <!-- Backdrop illustration area -->
  <rect class="backdrop" role="img" aria-label="Illustration of a teal city skyline under a cloudy blue sky with birds in flight" x="0" y="0" width="1200" height="456" fill="url(#scene-fill)"/>

  <!-- Brick wall -->
  <rect class="brick-wall" role="img" aria-label="Red brick wall" x="0" y="456" width="1200" height="153" fill="var(--brick)"/>
  <g class="pillars" role="img" aria-label="Grey brick pillars">
    <rect x="4" y="438" width="130" height="171" fill="var(--pillar)"/>
    <rect x="4" y="438" width="130" height="14" fill="var(--pillar-dark)"/>
    <rect x="522" y="438" width="136" height="171" fill="var(--pillar)"/>
    <rect x="522" y="438" width="136" height="14" fill="var(--pillar-dark)"/>
    <rect x="1009" y="438" width="152" height="171" fill="var(--pillar)"/>
    <rect x="1009" y="438" width="152" height="14" fill="var(--pillar-dark)"/>
  </g>

  <!-- Celebrate -->
  <g class="label label--celebrate">
    <rect class="label-shadow" x="18" y="74" width="540" height="104" rx="30"/>
    <rect x="26" y="62" width="540" height="104" rx="30" fill="var(--cream)"/>
    <text class="word word--celebrate" x="294" y="118" textLength="456" lengthAdjust="spacingAndGlyphs">Celebrate</text>
  </g>

  <!-- Create -->
  <g class="label label--create">
    <polygon class="label-shadow" points="310,220 652,220 622,322 280,322"/>
    <polygon points="318,208 660,208 630,312 289,312" fill="var(--cream)"/>
    <text class="word word--create" x="470" y="266" textLength="262" lengthAdjust="spacingAndGlyphs">Create</text>
  </g>

  <!-- Collaborate -->
  <g class="label label--collaborate">
    <rect class="label-shadow" x="68" y="356" width="512" height="116" rx="40"/>
    <rect x="78" y="342" width="512" height="116" rx="40" fill="var(--white)"/>
    <text class="word word--collaborate-shadow" x="335" y="403" textLength="444" lengthAdjust="spacingAndGlyphs">Collaborate</text>
    <text class="word word--collaborate" x="340" y="396" textLength="444" lengthAdjust="spacingAndGlyphs">Collaborate</text>
  </g>

  <!-- Innovate -->
  <g class="label label--innovate">
    <path class="label-shadow" d="M678 324 H1082 V328 a12 12 0 0 0 12 12 V402 a12 12 0 0 0 -12 12 V424 H678 V414 a12 12 0 0 0 -12 -12 V340 a12 12 0 0 0 12 -12 Z"/>
    <path d="M684 314 H1088 V320 a12 12 0 0 0 12 12 V394 a12 12 0 0 0 -12 12 V416 H684 V406 a12 12 0 0 0 -12 -12 V332 a12 12 0 0 0 12 -12 Z" fill="var(--silver)"/>
    <text class="word word--innovate" x="893" y="362" textLength="385" lengthAdjust="spacingAndGlyphs">Innovate</text>
  </g>

  <!-- Investigate -->
  <g class="label label--investigate">
    <rect class="label-shadow" x="710" y="507" width="442" height="76" rx="34"/>
    <rect x="716" y="499" width="442" height="76" rx="34" fill="var(--lavender)"/>
    <text class="word word--investigate" x="937" y="539" textLength="379" lengthAdjust="spacingAndGlyphs">INVESTIGATE</text>
  </g>
</svg>
</body>
</html>
```